Flyer-Design für Designer-Schmuck
Großartig - sehr gut !! Super zu frieden !!
Zielgruppe
Wir produzieren außergewöhnlichen und hochwertigen Designer-Schmuck aus Lüster-Bleikristallen für eine modebewusstes Publikum. Der Flyer wird als Beipack-Flyer unseren Versendungen beigefügt und enthält Informationen, sowie Hinweise für unsere Kunden über Morgenfalter, zu Nachhaltigkeit und Pflege.
Aufgabenstellung
nicht größer als DIN A5 | mindestens 2 oder mehr Seiten | Sollte die Aufteilung der Texte 6 Seiten erfordern sind auch 6 Seiten in Ordnung | Design und Layout sind sonst wenig Grenzen gesetzt - wir lassen uns gerne von Euren Vorschlägen begeistern, gerne aber mit Wiedererkennungswert zur Webseite https://morgenfalter-hamburg.de

```html
<!DOCTYPE html>
<html lang="de">
<head>
<meta charset="utf-8">
<title>Morgenfalter Hamburg – Flyer</title>
<link rel="stylesheet" href="https://fonts.googleapis.com/css2?family=Montserrat:wght@400;500;600;700&display=swap">
<style>
:root{
  --purple:#7b2a7f;
  --purple-light:#9b55a0;
  --purple-soft:#b27bb6;
  --paper:#ffffff;
  --stage:#f2f2f2;
  --ink:#4a4a4a;
  --ink-soft:#6d6d6d;
  --rule:#b98abd;
  --photo-a:#c9c0b8;
  --photo-b:#a89a8e;
  --photo-c:#d8cfc6;
}
*{box-sizing:border-box;margin:0;padding:0}
html,body{width:1200px;height:2400px;overflow:hidden}
body{background:var(--stage);font-family:"Montserrat",sans-serif;color:var(--ink);position:relative}
.spread{position:absolute;left:50px;width:1100px;height:780px;display:flex;box-shadow:0 6px 24px rgba(0,0,0,.15)}
.spread--outside{top:390px}
.spread--inside{top:1230px}
.page{position:relative;width:550px;height:780px;overflow:hidden}
.page--purple{background:var(--purple);color:#fff}
.page--white{background:var(--paper)}
.photo{position:absolute;background:linear-gradient(135deg,var(--photo-c),var(--photo-b));}
.photo--warm{background:linear-gradient(150deg,#e2d6cb,#b89c8a)}
.photo--cool{background:linear-gradient(150deg,#d9dde0,#9fa7ad)}

/* back cover */
.back__intro{position:absolute;left:90px;top:565px;width:420px}
.back__intro h3{font-size:14px;font-weight:700;margin-bottom:6px}
.back__intro p{font-size:9.5px;line-height:1.5;font-weight:500}
.back__intro p.strong{font-weight:700;margin-top:8px}
.back__rule{position:absolute;left:90px;top:660px;width:385px;border-top:1px solid var(--purple-soft)}
.back__contact{position:absolute;left:90px;top:672px;width:385px;display:flex;justify-content:space-between;font-size:6.5px;line-height:1.4}
.back__contact div{display:flex;gap:5px}
.back__contact svg{flex:none}
.back__url{position:absolute;left:0;width:550px;top:728px;text-align:center;font-size:15px;font-weight:600;padding-right:60px}

/* front cover */
.brand{position:absolute;top:38px;left:0;width:550px;display:flex;justify-content:center;align-items:center;gap:10px}
.brand__dot{width:26px;height:26px;border-radius:50%;background:#fff}
.brand__name{font-size:34px;font-weight:700;line-height:1}
.brand__city{font-size:12px;font-weight:500;letter-spacing:1px;text-align:center}
.front__tagline{position:absolute;top:670px;left:0;width:550px;text-align:center}
.front__tagline h2{font-size:22px;font-weight:500}
.front__tagline p{font-size:17px;letter-spacing:1px;margin-top:4px}

/* inside left */
.band{position:absolute;left:0;top:0;width:550px;height:140px;background:var(--purple);color:#fff;text-align:center;padding-top:48px}
.band h2{font-size:22px;font-weight:500}
.band p{font-size:16px;letter-spacing:1px;margin-top:2px}
.story{position:absolute;left:32px;top:160px;width:480px;font-size:10.5px;line-height:1.55;color:var(--ink)}
.story p+p{margin-top:10px}
.page-rule{position:absolute;border-top:1px solid var(--rule)}
.values{position:absolute;left:285px;top:505px;display:flex;flex-direction:column;gap:18px}
.tick-item{display:flex;align-items:flex-start;gap:12px}
.tick-item svg{flex:none}
.tick-item h4{font-size:15px;font-weight:400;line-height:1.1;color:var(--ink)}
.tick-item span{display:block;font-size:10px;line-height:1.25;color:var(--ink-soft)}
.foot-strip{position:absolute;left:0;bottom:0;width:550px;height:18px;background:var(--purple)}

/* inside right */
.section-head{position:absolute;left:0;width:550px;text-align:center;color:#3a3a3a}
.section-head h3{font-size:22px;font-weight:600}
.section-head p{font-size:16px;letter-spacing:1px;color:var(--purple)}
.lead{position:absolute;left:28px;width:500px;font-size:10.5px;line-height:1.45}
.grid{position:absolute;left:28px;width:500px;display:grid;grid-template-columns:1fr 1fr;gap:16px 18px}
.grid .tick-item h4{font-size:14px}
.grid .tick-item span{font-size:9px}
.pill{position:absolute;left:28px;width:494px;height:20px;border-radius:10px;background:var(--purple);color:#fff;font-size:9.5px;text-align:center;line-height:20px}
.notes{position:absolute;left:28px;top:692px;width:494px;font-size:8px;line-height:1.4;color:var(--ink-soft)}
.notes p+p{margin-top:6px}
.notes b{color:var(--ink)}
</style>
</head>
<body>

<!-- outside: back + front cover -->
<section class="spread spread--outside">
  <div class="page page--purple back-cover">
    <div class="back__intro">
      <h3>Lerne uns kennen</h3>
      <p>Auf unserer Website findest du unser gesamtes Sortiment – zum Beispiel<br>edle Halsketten, elegante Ohrringe und verspielte Armbänder.</p>
      <p class="strong">Wir freuen uns auf deinen Besuch!</p>
    </div>
    <div class="back__rule"></div>
    <div class="back__contact">
      <div>
        <svg width="9" height="11" viewBox="0 0 10 12"><path d="M5 0C2.5 0 .8 1.9.8 4.2 .8 7.3 5 12 5 12s4.2-4.7 4.2-7.8C9.2 1.9 7.5 0 5 0zm0 6a1.8 1.8 0 110-3.6A1.8 1.8 0 015 6z" fill="#fff"/></svg>
        <span><b>Morgenfalter Hamburg (Einzelunternehmung)</b><br>Lindenweg 12 | 21614 Musterfeld</span>
      </div>
      <div>
        <svg width="10" height="10" viewBox="0 0 12 12"><path d="M2.5 0.5l2 2.2-1 1.5c.8 1.6 2 2.8 3.6 3.6l1.5-1 2.2 2-1.2 2.2C5 10.8 1.2 7 .3 1.7z" fill="#fff"/></svg>
        <span><b>Telefon:</b><br>+49 (0)151 - 00 12 34 56</span>
      </div>
      <div>
        <svg width="11" height="9" viewBox="0 0 12 9"><rect x=".5" y=".5" width="11" height="8" fill="none" stroke="#fff"/><path d="M.5.5l5.5 4.5L11.5.5" fill="none" stroke="#fff"/></svg>
        <span><b>E-Mail:</b><br>info@morgenfalter-hamburg.de</span>
      </div>
    </div>
    <div class="back__url">www.morgenfalter-hamburg.de</div>
  </div>

  <div class="page page--purple front-cover">
    <div class="brand">
      <span class="brand__dot"></span>
      <div>
        <div class="brand__name">Morgenfalter</div>
        <div class="brand__city">HAMBURG</div>
      </div>
    </div>
    <div class="photo photo--warm" style="left:30px;top:145px;width:232px;height:148px" role="img" aria-label="Werktisch mit Schalen voller Kristalle"></div>
    <div class="photo photo--warm" style="left:30px;top:300px;width:232px;height:148px" role="img" aria-label="Nahaufnahme orangefarbener Lüsterkristalle"></div>
    <div class="photo photo--cool" style="left:30px;top:455px;width:232px;height:155px" role="img" aria-label="Kristallbehang eines Kronleuchters"></div>
    <div class="photo" style="left:270px;top:145px;width:250px;height:228px" role="img" aria-label="Atelierraum mit Kronleuchter und Schmuckbüste"></div>
    <div class="photo" style="left:270px;top:380px;width:250px;height:230px" role="img" aria-label="Arbeitsplatz im Atelier mit Regalen am Fenster"></div>
    <div class="front__tagline">
      <h2>Liebevoll gefertigte Schmuckstücke</h2>
      <p>SO EINZIGARTIG WIE DU</p>
    </div>
  </div>
</section>

<!-- inside spread -->
<section class="spread spread--inside">
  <div class="page page--white inside-left">
    <div class="band">
      <h2>Einzigartige, luxuriöse Schmuckstücke</h2>
      <p>FÜR DICH!</p>
    </div>
    <div class="story">
      <p>Mit den Schmuckstücken von Morgenfalter Hamburg bewahrst du einen Teil einer magisch anmutenden Vergangenheit und bringst zugleich Eleganz und Luxus in deinen Alltag.</p>
      <p>Sicher kennst du die großen, glitzernden Kronleuchter, die in prunkvollen Schlössern hängen und ihre Umgebung mit Schönheit, Glanz und Freude füllen. Seit Generationen begleiten und faszinieren sie uns, tragen Geheimnisse und Geschichten in sich und haben besondere Momente miterlebt.</p>
      <p>Diesen Glanz und diese Erinnerung an die Geschichten alter Zeiten fangen wir in den individuell gefertigten Miniatur-Lüstern ein, welche die meisten der Morgenfalter-Schmuckstücke zieren. Zusätzlich wählen wir mit großer Sorgfalt einzelne Kristalle aus und verarbeiten beide Elemente zu edlen, wahrlich einzigartigen Schmuckstücken.</p>
      <p>Ob kraftvoll in intensiven Farben oder zeitlos und dezent: Mit Morgenfalter wird dein Leben ein bisschen mystischer, luxuriöser oder einfach schöner – unsere Art, unsere Liebe zum Lüster mit dir zu teilen.</p>
    </div>
    <div class="page-rule" style="left:32px;top:470px;width:480px"></div>
    <div class="photo" style="left:32px;top:490px;width:225px;height:272px" role="img" aria-label="Atelier mit Kronleuchter, Spiegeln und Schmuckbüste"></div>
    <div class="values">
      <div class="tick-item"><svg width="24" height="24" viewBox="0 0 24 24"><circle cx="12" cy="12" r="12" fill="var(--purple)"/><path d="M7 12.5l3.2 3.2L17 9" fill="none" stroke="#fff" stroke-width="2.2"/></svg><div><h4>einzigartig</h4><span>sind unverwechselbare Einzelstücke</span></div></div>
      <div class="tick-item"><svg width="24" height="24" viewBox="0 0 24 24"><circle cx="12" cy="12" r="12" fill="var(--purple)"/><path d="M7 12.5l3.2 3.2L17 9" fill="none" stroke="#fff" stroke-width="2.2"/></svg><div><h4>nachhaltig</h4><span>werden unter hohen Anforderungen<br>an Nachhaltigkeit produziert</span></div></div>
      <div class="tick-item"><svg width="24" height="24" viewBox="0 0 24 24"><circle cx="12" cy="12" r="12" fill="var(--purple)"/><path d="M7 12.5l3.2 3.2L17 9" fill="none" stroke="#fff" stroke-width="2.2"/></svg><div><h4>handgemacht</h4><span>werden von Hand gearbeitet</span></div></div>
      <div class="tick-item"><svg width="24" height="24" viewBox="0 0 24 24"><circle cx="12" cy="12" r="12" fill="var(--purple)"/><path d="M7 12.5l3.2 3.2L17 9" fill="none" stroke="#fff" stroke-width="2.2"/></svg><div><h4>qualität</h4><span>aus echten Kristallen und<br>925er Sterlingsilber</span></div></div>
    </div>
    <div class="foot-strip"></div>
  </div>

  <div class="page page--white inside-right">
    <div class="photo" style="left:0;top:0;width:268px;height:140px" role="img" aria-label="Regale mit Schmuck am Atelierfenster"></div>
    <div class="photo photo--warm" style="left:276px;top:0;width:274px;height:140px" role="img" aria-label="Kronleuchter im Verkaufsraum"></div>

    <div class="section-head" style="top:158px"><h3>unser Nachhaltigkeitsversprechen</h3><p>NACHHALTIGKEIT IST UNS WICHTIG</p></div>
    <p class="lead" style="top:222px">Es ist uns wichtig, unseren Beitrag zu den hohen Klimazielen unseres Landes zu leisten. Deshalb setzen wir folgende Maßnahmen für mehr Nachhaltigkeit um:</p>
    <div class="grid" style="top:262px">
      <div class="tick-item"><svg width="22" height="22" viewBox="0 0 24 24"><circle cx="12" cy="12" r="12" fill="var(--purple)"/><path d="M7 12.5l3.2 3.2L17 9" fill="none" stroke="#fff" stroke-width="2.2"/></svg><div><h4>recycling</h4><span>wir verwenden zum großen Teil<br>wiederverwendete Kristalle</span></div></div>
      <div class="tick-item"><svg width="22" height="22" viewBox="0 0 24 24"><circle cx="12" cy="12" r="12" fill="var(--purple)"/><path d="M7 12.5l3.2 3.2L17 9" fill="none" stroke="#fff" stroke-width="2.2"/></svg><div><h4>regional</h4><span>unsere Fassung (in Form eines Lüsters)<br>wird regional gefertigt</span></div></div>
      <div class="tick-item"><svg width="22" height="22" viewBox="0 0 24 24"><circle cx="12" cy="12" r="12" fill="var(--purple)"/><path d="M7 12.5l3.2 3.2L17 9" fill="none" stroke="#fff" stroke-width="2.2"/></svg><div><h4>rücknahme</h4><span>sende die Acrylplatten zurück und<br>wir verwenden sie für unsere Muster und Ausstellungsstücke</span></div></div>
      <div class="tick-item"><svg width="22" height="22" viewBox="0 0 24 24"><circle cx="12" cy="12" r="12" fill="var(--purple)"/><path d="M7 12.5l3.2 3.2L17 9" fill="none" stroke="#fff" stroke-width="2.2"/></svg><div><h4>nachhaltig</h4><span>werden unter hohen Anforderungen<br>an Nachhaltigkeit produziert</span></div></div>
    </div>
    <div class="pill" style="top:392px">Die Gravuren führen wir selbst durch und dadurch entfallen unnötige Transportwege.</div>
    <div class="page-rule" style="left:28px;top:430px;width:494px"></div>

    <div class="section-head" style="top:448px"><h3>Pflegetipps &amp; Sicherheitshinweise</h3></div>
    <div class="grid" style="top:500px">
      <div class="tick-item"><svg width="22" height="22" viewBox="0 0 24 24"><circle cx="12" cy="12" r="12" fill="var(--purple)"/><rect x="7" y="8" width="10" height="9" rx="1.5" fill="none" stroke="#fff" stroke-width="1.6"/><path d="M9 8V6.5h6V8" fill="none" stroke="#fff" stroke-width="1.6"/></svg><div><h4>Morgenfalterglas</h4><span>schützt vor äußeren Einflüssen und<br>erhält die Schönheit und den Glanz<br>deiner Schmuckstücke</span></div></div>
      <div class="tick-item"><svg width="22" height="22" viewBox="0 0 24 24"><circle cx="12" cy="12" r="12" fill="var(--purple)"/><path d="M12 5.5c-2.5 3.5-4.5 6-4.5 8.2a4.5 4.5 0 009 0c0-2.2-2-4.7-4.5-8.2z" fill="none" stroke="#fff" stroke-width="1.6"/></svg><div><h4>Pflegehinweis</h4><span>verwende ein Silberputztuch oder<br>Silberbad, wenn dein Schmuck angelaufen ist</span></div></div>
    </div>
    <div class="pill" style="top:652px">Perlen müssen vor der Reinigung abgenommen werden. Kristalle werden nicht geschädigt.</div>
    <div class="notes">
      <p><b>Wichtig:</b> Da die Schmuckstücke verschluckbare Kleinteile enthalten, bewahre sie bitte außerhalb der Reichweite von Kindern unter drei Jahren auf. Kristall und Glas sind zerbrechlich und müssen vor Stoß und Schlag geschützt werden.</p>
      <p><b>Bitte beachte:</b> Die Kristalle können aufgrund ihres Alters einzelne Gebrauchsspuren aufweisen. Diese sind Teil ihrer Vergangenheit und machen sie nicht weniger schön, sondern verleihen ihnen im Gegenteil eine authentische, lebendige Einzigartigkeit.</p>
    </div>
    <div class="foot-strip"></div>
  </div>
</section>

</body>
</html>
```